Company truck branding

I'm looking for a clean wrap design for my company vehicles and trailers. It needs to fit our branding based on logo. Most of our trucks and trailers are grey but we do have white trucks also. You can visit our website Verodalandscaping.com or our instagram at verodalandscaping

Industry/Entity Type

Landscaping

Font styles to use
Serif
Sans Serif

Colors

Designer to choose only greyscale colors for use in the design.

Requirements
Must have
• Want a Clean MODERN DESIGN
Should not have
• Don’t want grass or anything that is not on my logo.

```html
<!DOCTYPE html>
<html lang="en">
<head>
<meta charset="utf-8">
<title>Veroda Landscaping – Truck Wrap</title>
<link href="https://fonts.googleapis.com/css2?family=Archivo:wght@400;500;700;800&display=swap" rel="stylesheet">
<style>
  :root {
    --page: #e4e4e2;
    --wrap: #2a2a2a;
    --frame: #b9bcbf;
    --frame-dark: #8f9397;
    --gold: #a98b5f;
    --white: #f4f2ee;
    --silhouette: rgba(14, 14, 14, .75);
  }
  * { box-sizing: border-box; margin: 0; padding: 0; }
  html, body { width: 1200px; height: 801px; overflow: hidden; }
  body { background: var(--page); font-family: "Archivo", sans-serif; color: var(--white); position: relative; }

  .wrap-panel {
    position: absolute; left: 20px; top: 175px; width: 1160px; height: 450px;
    background: var(--wrap); border: 6px solid var(--frame); border-radius: 4px; overflow: hidden;
  }

  /* scenery placeholders blend softly into the panel */
  .scenery { position: absolute; pointer-events: none; }
  .scenery-ridge {
    left: 20px; top: 250px; width: 640px; height: 190px;
    background: radial-gradient(ellipse 50% 50% at 50% 70%, var(--silhouette) 0%, rgba(14,14,14,.35) 55%, transparent 100%);
  }
  .scenery-pines {
    left: 640px; top: 60px; width: 500px; height: 380px;
    background: radial-gradient(ellipse 50% 55% at 50% 62%, var(--silhouette) 0%, rgba(14,14,14,.4) 55%, transparent 100%);
  }

  .ground-curve { position: absolute; left: 640px; top: 360px; width: 480px; height: 84px; }

  .side-door {
    position: absolute; left: 684px; top: -6px; width: 244px; height: 450px;
    border-left: 14px solid var(--frame); border-right: 14px solid var(--frame);
  }
  .side-door::after {
    content: ""; position: absolute; left: 10px; right: 8px; top: 22px; bottom: 10px;
    border: 4px solid var(--frame-dark); border-radius: 3px;
  }

  .brand { position: absolute; text-align: center; font-weight: 700; color: var(--white); line-height: 1; }
  .brand-mark { display: block; width: 14px; height: 14px; margin: 0 auto 10px; background: var(--gold); border-radius: 50%; }
  .brand-name { display: block; letter-spacing: .06em; }
  .brand-tagline { display: block; letter-spacing: .45em; margin-top: 8px; padding-left: .45em; }
  .brand-left { left: 14px; top: 78px; width: 200px; }
  .brand-left .brand-name { font-size: 40px; }
  .brand-left .brand-tagline { font-size: 12px; }
  .brand-right { left: 930px; top: 52px; width: 210px; }
  .brand-right .brand-name { font-size: 42px; }
  .brand-right .brand-tagline { font-size: 12px; }

  .services-tag {
    position: absolute; left: 234px; top: 30px; background: var(--gold);
    font-weight: 800; font-size: 22px; padding: 9px 14px 8px; transform: rotate(-2deg);
  }
  .service { position: absolute; display: flex; align-items: center; gap: 14px; font-size: 20px; font-weight: 400; line-height: 1.02; }
  .service-icon { width: 36px; height: 36px; flex: none; }
  .service-hardscapes { left: 234px; top: 100px; }
  .service-maintenance { left: 234px; top: 146px; }
  .service-design { left: 452px; top: 66px; }
  .service-health { left: 452px; top: 130px; }

  .contact-pill {
    position: absolute; left: 14px; top: 360px; display: flex; align-items: center; gap: 6px;
    background: var(--white); color: var(--gold); border-radius: 12px; padding: 4px 12px;
    font-weight: 800; font-size: 27px; letter-spacing: -.03em; white-space: nowrap;
  }
  .contact-pill svg { width: 24px; height: 24px; flex: none; }
</style>
</head>
<body>
  <section class="wrap-panel">
    <div class="scenery scenery-ridge" role="img" aria-label="Mountain ridge outline with pine tree silhouettes"></div>
    <div class="scenery scenery-pines" role="img" aria-label="Tall pine tree silhouettes"></div>
    <svg class="ground-curve" viewBox="0 0 480 84" aria-hidden="true">
      <path d="M0 60 Q160 -10 480 84 L0 84 Z" fill="var(--gold)"/>
    </svg>

    <div class="side-door" aria-hidden="true"></div>

    <div class="brand brand-left"><span class="brand-mark"></span><span class="brand-name">VERODA</span><span class="brand-tagline">LANDSCAPING</span></div>
    <div class="brand brand-right"><span class="brand-mark"></span><span class="brand-name">VERODA</span><span class="brand-tagline">LANDSCAPING</span></div>

    <div class="services-tag">SERVICES</div>

    <div class="service service-hardscapes">
      <svg class="service-icon" viewBox="0 0 36 36" aria-hidden="true"><rect x="2" y="26" width="32" height="8" rx="1" fill="var(--white)"/><path d="M28 4l-8 18" stroke="var(--white)" stroke-width="3" stroke-linecap="round"/><path d="M16 20l6 3-3 5-5-3z" fill="var(--white)"/><path d="M8 24v-8m0 0c-4 0-5-3-5-5 3 0 5 2 5 5zm0 0c4 0 5-3 5-5-3 0-5 2-5 5z" stroke="var(--white)" stroke-width="2" fill="var(--white)"/></svg>
      <span>Hardscapes</span>
    </div>
    <div class="service service-maintenance">
      <svg class="service-icon" viewBox="0 0 36 36" aria-hidden="true"><path d="M2 34V24q16-8 32 0v10z" fill="var(--white)"/><path d="M2 22q10-6 20-2" stroke="var(--white)" stroke-width="2" fill="none"/><circle cx="26" cy="8" r="5" fill="var(--white)"/><rect x="25" y="12" width="2" height="8" fill="var(--white)"/><path d="M6 20l4-10 4 10z" fill="var(--white)"/></svg>
      <span>Landscape<br>Maintenance</span>
    </div>
    <div class="service service-design">
      <svg class="service-icon" viewBox="0 0 36 36" aria-hidden="true"><circle cx="22" cy="21" r="12" fill="var(--white)"/><path d="M15 27l14-14M17 15l12 12" stroke="var(--wrap)" stroke-width="2.5"/><circle cx="8" cy="10" r="6" fill="var(--white)"/><rect x="7" y="15" width="2" height="17" fill="var(--white)"/></svg>
      <span>Design<br>Build</span>
    </div>
    <div class="service service-health">
      <svg class="service-icon" viewBox="0 0 36 36" aria-hidden="true"><path d="M15 2h6v5h5v6h-5v5h-6v-5h-5V7h5z" fill="var(--white)"/><path d="M18 34C8 34 2 28 3 18c9 0 15 6 15 16zM18 34c10 0 16-6 15-16-9 0-15 6-15 16z" fill="var(--white)"/><path d="M18 34L9 23M18 34l9-11" stroke="var(--wrap)" stroke-width="1.5"/></svg>
      <span>Plant<br>Healthcare</span>
    </div>

    <div class="contact-pill">
      <svg viewBox="0 0 24 24" aria-hidden="true"><path d="M6.6 10.8a15.1 15.1 0 0 0 6.6 6.6l2.2-2.2c.3-.3.7-.4 1-.2 1.1.4 2.3.6 3.6.6.6 0 1 .4 1 1V20c0 .6-.4 1-1 1A17 17 0 0 1 3 4c0-.6.4-1 1-1h3.5c.6 0 1 .4 1 1 0 1.3.2 2.5.6 3.6.1.3 0 .7-.2 1z" fill="currentColor"/></svg>
      <span>208-555-0147</span>
      <svg viewBox="0 0 24 24" aria-hidden="true"><circle cx="12" cy="12" r="10" fill="currentColor"/><path d="M2 12h20M12 2c3 3 3 17 0 20M12 2c-3 3-3 17 0 20" stroke="var(--white)" stroke-width="1.5" fill="none"/></svg>
      <span>verodalandscaping.com</span>
    </div>
  </section>
</body>
</html>
```